KT Forge Business Card

I would like a business card similar to this
https://www.artbidhub.example/design/4817203
with my info and a picture of my rifle. You can use something like this
https://www.snapboardly.example/pin/381920475566120847/visual-search/?cropSource=6&h=476&w=268&x=12&y=12
or
https://www.snapboardly.example/pin/529174006381742915/

I have a logo, it is a shepperds staff. I build custom rifles and do Law Enforcement sales. Some where on the card it needs to say something like, "Custom AR's built correctly", "All rifles come with honed uppers and bedded barrels", "All rifles are fully tested and come with a 3 shot card", "Law Enforcement models are available", "Tactical Equipment Consulting", "One stop shop for all tactical equipment"

Business Name: KT Forge LLC
Name: Milo Hartwell
Phone: (555) 014-3382
Email: milo.ktforge@mailbox-demo.net
Address: 2891 Larkspur Ln., Alder Falls, NC, 29815

Just use the concept of the staff in the attachments the other stuff is not related

```html
<!DOCTYPE html>
<html lang="en">
<head>
<meta charset="utf-8">
<title>KT Forge Business Card</title>
<link rel="stylesheet" href="https://fonts.googleapis.com/css2?family=Open+Sans:wght@400;600;700;800&display=swap">
<style>
  :root {
    --page-bg: #e6e6e6;
    --card-dark: #161616;
    --card-dark-edge: #2a2a2a;
    --brand-dark-text: #4a4a4a;
    --card-light: #ffffff;
    --ink-navy: #1f2b3c;
    --ink-body: #3b3f45;
    --rifle-tone-a: #d9dbde;
    --rifle-tone-b: #5f646b;
    --rifle-tone-c: #9c9585;
  }
  * { box-sizing: border-box; margin: 0; padding: 0; }
  html, body {
    width: 1200px;
    height: 960px;
    overflow: hidden;
    background: var(--page-bg);
    font-family: "Open Sans", Arial, sans-serif;
  }
  .canvas {
    width: 1200px;
    height: 960px;
    display: flex;
    flex-direction: column;
    align-items: center;
    justify-content: center;
    gap: 50px;
  }
  .card {
    width: 700px;
    height: 400px;
    border-radius: 22px;
    position: relative;
    overflow: hidden;
    box-shadow: 0 6px 18px rgba(0,0,0,0.18);
  }

  /* Back side */
  .card--back {
    background: linear-gradient(160deg, var(--card-dark-edge) 0%, var(--card-dark) 55%);
    display: flex;
    align-items: center;
    justify-content: center;
  }
  .brand-mark {
    font-size: 46px;
    font-weight: 600;
    letter-spacing: 3px;
    color: var(--brand-dark-text);
    text-transform: uppercase;
  }

  /* Front side */
  .card--front { background: var(--card-light); }
  .rifle-photo {
    position: absolute;
    left: 315px;
    top: 22px;
    width: 365px;
    height: 240px;
    border-radius: 6px;
    background: radial-gradient(ellipse at 55% 50%, var(--rifle-tone-b) 0%, var(--rifle-tone-c) 45%, var(--rifle-tone-a) 80%, var(--card-light) 100%);
  }
  .contact-block {
    position: absolute;
    left: 40px;
    top: 90px;
    width: 330px;
    color: var(--ink-body);
  }
  .holder-name {
    font-size: 26px;
    font-weight: 800;
    color: var(--ink-navy);
    letter-spacing: 0.3px;
    margin-bottom: 8px;
  }
  .company-name {
    font-size: 17px;
    font-weight: 700;
    color: var(--ink-navy);
    line-height: 1.2;
  }
  .address { font-size: 15px; line-height: 1.3; margin-bottom: 10px; }
  .contact-list { list-style: none; margin-bottom: 12px; }
  .contact-list li {
    display: flex;
    align-items: center;
    gap: 10px;
    font-size: 14.5px;
    line-height: 1.35;
    white-space: nowrap;
  }
  .contact-list svg { width: 13px; height: 13px; fill: var(--ink-navy); flex: none; }
  .service-list { list-style: none; }
  .service-list li {
    position: relative;
    padding-left: 18px;
    font-size: 12.5px;
    line-height: 1.4;
    white-space: nowrap;
  }
  .service-list li::before {
    content: "";
    position: absolute;
    left: 3px;
    top: 7px;
    width: 5px;
    height: 5px;
    border-radius: 50%;
    background: var(--ink-navy);
  }
</style>
</head>
<body>
<main class="canvas">
  <section class="card card--back">
    <span class="brand-mark">KT Forge</span>
  </section>

  <section class="card card--front">
    <div class="rifle-photo" role="img" aria-label="Photo of a custom AR rifle with suppressor, optic and tan furniture"></div>
    <div class="contact-block">
      <h1 class="holder-name">MILO HARTWELL</h1>
      <p class="company-name">KT Forge LLC</p>
      <p class="address">2891 Larkspur Ln.<br>Alder Falls, NC, 29815</p>
      <ul class="contact-list">
        <li>
          <svg viewBox="0 0 24 24" aria-hidden="true"><path d="M6.6 10.8a15.1 15.1 0 0 0 6.6 6.6l2.2-2.2a1 1 0 0 1 1-.25 11.4 11.4 0 0 0 3.6.57 1 1 0 0 1 1 1V20a1 1 0 0 1-1 1A17 17 0 0 1 3 4a1 1 0 0 1 1-1h3.5a1 1 0 0 1 1 1c0 1.25.2 2.45.57 3.570a1 1 0 0 1-.25 1z"/></svg>
          (555) 014-3382
        </li>
        <li>
          <svg viewBox="0 0 24 24" aria-hidden="true"><path d="M2 5h20v14H2z"/><path d="M3 6.5l9 7 9-7" stroke="#fff" stroke-width="1.8" fill="none"/></svg>
          milo.ktforge@mailbox-demo.net
        </li>
        <li>
          <svg viewBox="0 0 24 24" aria-hidden="true"><circle cx="12" cy="12" r="10"/><path d="M2 12h20M12 2c3 3 3 17 0 20M12 2c-3 3-3 17 0 20" stroke="#fff" stroke-width="1.6" fill="none"/></svg>
          www.ktforge.com
        </li>
      </ul>
      <ul class="service-list">
        <li>Custom ARs built correctly</li>
        <li>All rifles built with honed uppers &amp; bedded barrels</li>
        <li>Rifles are fully tested &amp; include a 3 shot grouping card</li>
        <li>Law Enforcement models available</li>
        <li>Tactical Equipment Consulting</li>
        <li>One stop shop for all tactical equipment</li>
      </ul>
    </div>
  </section>
</main>
</body>
</html>
```